Web design for development company

We would like web, logo and business card designs for a construction and development company in Halifax, Nova Scotia called "R & K Group Developments Limited".

We would like the web design to be professional, and luxurious . The colours should be professional/more mature and easy to read. The website should include: home page, about page, projects, and contact.

The logo design should also be professional in appearance and minimal/not too busy with the company name included. I have attached a few logos that I like for inspiration.

We would like the cards to be double sided with one side being the logo and name of the company. The other side of the card should include the following: logo, company name, name, title, mobile number, office number, fax, email, and website link.

Target Market(s)

general public, potential clients/business partners

Industry/Entity Type

Construction and Development

Coding

Coded - Design and coding required

Number of Pages Required

5+ page

Font styles to use
Serif
Decorative

Requirements
Must have
• the website type i want to receive is coded (the uncoded won't correct to coded on the brief page for some reason) )
Should not have
• playful elements that make the website less professional.Unreadable logos and writing.

```html
<!DOCTYPE html>
<html lang="en">
<head>
<meta charset="utf-8">
<title>R & K Group Developments Limited</title>
<link rel="stylesheet" href="https://fonts.googleapis.com/css2?family=Josefin+Sans:wght@400;600;700&family=Mulish:wght@400;600;700&display=swap">
<style>
:root{
  --blue:#1a7fd4;
  --blue-deep:#1270c2;
  --ink:#111418;
  --text:#2b2f33;
  --muted:#6b7178;
  --line:#c9ccd0;
  --paper:#ffffff;
  --mist:#e9eaec;
  --footer:#262626;
  --footer-text:#d8d8d8;
}
*{box-sizing:border-box;margin:0;padding:0}
html,body{width:1200px;height:3532px;overflow:hidden}
body{position:relative;background:var(--paper);font-family:"Mulish",Arial,sans-serif;color:var(--text)}
.abs{position:absolute}
.display{font-family:"Josefin Sans",Arial,sans-serif;font-weight:700;color:var(--ink);text-transform:uppercase}

/* hero */
.hero{left:0;top:0;width:1200px;height:695px;background:linear-gradient(180deg,#c7d3df 0%,#9fb0c2 30%,#8d96a0 55%,#5c6167 72%,#3a3d40 100%)}
.brand{left:132px;top:30px;display:flex;align-items:center;gap:14px}
.brand-mark{width:66px;height:66px;border:2px solid var(--ink);border-radius:50%}
.brand-name{font-family:"Josefin Sans",sans-serif;color:var(--ink);font-size:28px;font-weight:400;line-height:1}
.brand-name small{display:block;font-size:14px;letter-spacing:.5px;margin-top:6px}
.nav{right:132px;top:40px;display:flex;gap:46px}
.nav a{font-family:"Josefin Sans",sans-serif;font-weight:600;font-size:16px;color:var(--ink);text-decoration:none;letter-spacing:.5px}
.hero-title{left:0;width:1200px;top:133px;text-align:center;font-size:25px;letter-spacing:.6px}
.hero-sub{left:0;width:1200px;top:172px;text-align:center;font-size:19px;color:var(--ink)}
.btn-solid{left:540px;top:217px;width:120px;height:38px;background:var(--blue);color:#fff;font-family:"Josefin Sans",sans-serif;font-weight:700;font-size:13px;display:flex;align-items:center;justify-content:center;letter-spacing:.4px}
.dots{left:562px;top:649px;display:flex;gap:11px;align-items:center}
.dots span{width:6px;height:6px;border-radius:50%;background:#fff}
.dots .on{width:11px;height:11px;border:2px solid #fff;background:var(--blue)}

/* intro */
.intro-photo{left:0;top:716px;width:569px;height:593px;background:linear-gradient(160deg,#b9c8d8 0%,#6e7c8a 35%,#3c3f44 65%,#8a6a3a 85%,#4a4a44 100%)}
.eyebrow{left:621px;top:818px;font-family:"Josefin Sans",sans-serif;font-weight:600;font-size:19px;color:var(--ink);letter-spacing:.5px}
.intro-title{left:621px;top:856px;font-size:41px;line-height:50px;letter-spacing:1px}
.intro-copy{left:624px;top:1028px;width:420px;font-size:14.5px;line-height:20px;color:var(--ink)}
.btn-outline{border:1.5px solid var(--blue);color:var(--blue);font-family:"Montserrat","Josefin Sans",sans-serif;font-weight:700;font-size:12.5px;display:flex;align-items:center;justify-content:center;background:#fff}
.btn-arrow{position:absolute}

/* services */
.section-title{left:0;width:1200px;text-align:center;top:1400px;font-size:34px;letter-spacing:1.5px}
.services-band{left:0;top:1470px;width:1200px;height:680px}
.card{background:#fff;width:454px;height:256px;box-shadow:0 2px 18px rgba(0,0,0,.06)}
.card-head{position:absolute;left:50px;top:32px;display:flex;align-items:center}
.card-icon{width:70px;height:62px}
.card-rule{width:2px;height:54px;background:var(--ink);margin:0 22px 0 22px}
.card-title{font-family:"Josefin Sans",sans-serif;font-weight:600;font-size:22px;letter-spacing:4px;color:var(--ink);text-transform:uppercase;padding-top:4px}
.card-copy{position:absolute;left:52px;top:125px;width:355px;font-size:13.2px;line-height:20px;color:var(--ink)}

/* portfolio */
.portfolio-title{left:131px;top:2224px;font-size:28px;line-height:42px;letter-spacing:1px}
.tile{width:293px;height:214px}
.timeline{left:764px;top:2336px;width:2px;height:442px;background:var(--line)}
.timeline-active{left:762px;top:2365px;width:6px;height:117px;background:var(--blue);border-radius:3px}
.entry{left:808px;width:245px}
.entry h3{font-family:"Josefin Sans",sans-serif;font-weight:700;font-size:14.5px;letter-spacing:.5px;color:var(--ink);text-transform:uppercase}
.entry p{font-size:12.5px;line-height:17.5px;margin-top:12px;color:var(--ink)}
.entry.active h3,.entry.active p{color:var(--blue)}
.divider{left:808px;width:261px;height:1.5px;background:#9aa0a6}

/* cta */
.footer{left:0;top:3023px;width:1200px;height:509px;background:var(--footer)}
.cta{left:129px;top:2857px;width:941px;height:315px;background:linear-gradient(180deg,var(--blue) 0%,#1a78c8 45%,#1668b0 60%,var(--blue-deep) 100%)}
.cta-title{left:129px;width:941px;top:2930px;text-align:center;color:#fff;font-size:28.5px;line-height:41px;letter-spacing:1.2px}
.cta-btn{left:494px;top:3038px;width:204px;height:56px;background:#fff;color:var(--blue);font-family:"Josefin Sans",sans-serif;font-weight:700;font-size:18px;letter-spacing:1px;display:flex;align-items:center;justify-content:center;gap:12px}

/* footer */
.foot-mark{left:133px;top:3247px;width:160px;height:160px;border:2px solid #fff;border-radius:50%}
.foot-name{left:133px;top:3300px;width:160px;text-align:center;color:#fff;font-family:"Josefin Sans",sans-serif;font-weight:700;font-size:30px;line-height:34px;letter-spacing:1px}
.foot-head{font-family:"Josefin Sans",sans-serif;font-weight:700;font-size:13px;color:#fff;letter-spacing:.6px}
.foot-links{left:395px;top:3275px;font-size:12px;line-height:20px;color:var(--footer-text);list-style:none}
.foot-item{display:flex;gap:12px;align-items:flex-start;font-size:12px;line-height:16px;color:var(--footer-text)}
.foot-ico{width:22px;height:22px;border-radius:50%;background:#fff;flex:none;margin-top:3px;display:flex;align-items:center;justify-content:center}
.foot-rule{left:133px;top:3450px;width:934px;height:1px;background:#444}
.copyright{left:0;width:1200px;top:3492px;text-align:center;font-size:9.5px;color:var(--footer-text)}
</style>
</head>
<body>

<!-- hero -->
<div class="abs hero" role="img" aria-label="Photograph of a modern low-rise commercial building with glass frontage under a cloudy evening sky"></div>
<div class="abs brand">
  <div class="brand-mark"></div>
  <div class="brand-name">R &amp; K GROUP<small>DEVELOPMENTS LIMITED</small></div>
</div>
<nav class="abs nav"><a href="#">HOME</a><a href="#">ABOUT</a><a href="#">PROJECTS</a><a href="#">CONTACT</a></nav>
<h1 class="abs display hero-title">Commercial Construction and Development</h1>
<p class="abs hero-sub">Lorem Ipsum is simply dummy text of the printing</p>
<a class="abs btn-solid">READ MORE</a>
<div class="abs dots"><span></span><span></span><span class="on"></span><span></span><span></span></div>

<!-- intro -->
<div class="abs intro-photo" role="img" aria-label="Photograph of a multi-storey glass and dark-panel office building at sunset"></div>
<div class="abs eyebrow">INTRODUCTION</div>
<h2 class="abs display intro-title">R &amp; K Group<br>Developments<br>Limited.</h2>
<p class="abs intro-copy">Sed ut perspiciatis unde omnis iste natus error sit voluptatem accusantium doloremque laudantium, totam rem aperiam, eaque ipsa quae ab illo inventore veritatis et quasi architecto beatae vitae dicta sunt explicabo. Nemo enim ipsam voluptatem quia voluptas sit aspernatur aut odit aut fugi.</p>
<a class="abs btn-outline" style="left:629px;top:1168px;width:118px;height:39px;">READ MORE</a>
<svg class="btn-arrow" style="left:738px;top:1176px" width="34" height="24" viewBox="0 0 34 24"><path d="M0 12H32M23 3l9 9-9 9" fill="none" stroke="#1a7fd4" stroke-width="1.5"/></svg>

<!-- services -->
<h2 class="abs display section-title">What We Do</h2>
<svg class="abs services-band" viewBox="0 0 1200 680" preserveAspectRatio="none" role="img" aria-label="Soft grey background with blurred light">
  <defs><linearGradient id="band" x1="0" y1="0" x2="1" y2="1"><stop offset="0" stop-color="#eeeff0"/><stop offset="1" stop-color="#e2e3e5"/></linearGradient></defs>
  <polygon points="0,330 1200,0 1200,680 0,680" fill="url(#band)"/>
</svg>

<div class="abs card" style="left:129px;top:1515px">
  <div class="card-head">
    <svg class="card-icon" viewBox="0 0 70 62" fill="none" stroke="#111" stroke-width="2"><path d="M4 12h62M14 12l12-10 12 10M22 12v48M30 12v48M22 24l8 8M30 24l-8 8M22 40l8 8M30 40l-8 8M14 60h26M58 12v14M54 26h8v6h-8z"/></svg>
    <div class="card-rule"></div><div class="card-title">Construction</div>
  </div>
  <p class="card-copy">Sed ut perspiciatis unde omnis iste natus error sit voluptatem accusantium doloremque laudantium, totam rem aperiam, eaque ipsa quae ab illo inventore eos qui ratione voluptatem sequi nesciunt. Neque porro quisquam est, qui dolorem ipsum.</p>
</div>
<div class="abs card" style="left:611px;top:1544px">
  <div class="card-head">
    <svg class="card-icon" viewBox="0 0 70 62" fill="none" stroke="#111" stroke-width="2"><path d="M12 8l44 44-4 6-6-2L8 14zM46 8l12 12-36 36-12-12zM26 26l4 4M32 20l4 4M38 14l4 4"/></svg>
    <div class="card-rule"></div><div class="card-title">Design Build</div>
  </div>
  <p class="card-copy">Sed ut perspiciatis unde omnis iste natus error sit voluptatem accusantium doloremque laudantium, totam rem aperiam, eaque ipsa quae ab illo inventore eos qui ratione voluptatem sequi nesciunt. Neque porro quisquam est, qui dolorem ipsum.</p>
</div>
<div class="abs card" style="left:129px;top:1811px">
  <div class="card-head">
    <svg class="card-icon" viewBox="0 0 70 62" fill="none" stroke="#111" stroke-width="2"><path d="M14 34v-6a21 21 0 0 1 42 0v6"/><rect x="10" y="32" width="8" height="14" rx="3"/><rect x="52" y="32" width="8" height="14" rx="3"/><path d="M56 46c0 8-8 10-18 10"/><rect x="30" y="53" width="9" height="6" rx="3"/></svg>
    <div class="card-rule"></div><div class="card-title">Support</div>
  </div>
  <p class="card-copy">Sed ut perspiciatis unde omnis iste natus error sit voluptatem accusantium doloremque laudantium, totam rem aperiam, eaque ipsa quae ab illo inventore eos qui ratione voluptatem sequi nesciunt. Neque porro quisquam est, qui dolorem ipsum.</p>
</div>
<div class="abs card" style="left:611px;top:1841px">
  <div class="card-head">
    <svg class="card-icon" viewBox="0 0 70 62" fill="none" stroke="#111" stroke-width="2"><path d="M12 10l20-6 26 8v46H12z"/><path d="M12 10l20 6 26-4M32 16v42"/><path d="M17 22h8v8h-8zM17 36h8v8h-8zM37 24h6v8h-6zM47 22h6v8h-6zM37 38h6v8h-6zM47 36h6v8h-6z"/></svg>
    <div class="card-rule"></div><div class="card-title">Development</div>
  </div>
  <p class="card-copy">Sed ut perspiciatis unde omnis iste natus error sit voluptatem accusantium doloremque laudantium, totam rem aperiam, eaque ipsa quae ab illo inventore eos qui ratione voluptatem sequi nesciunt. Neque porro quisquam est, qui dolorem ipsum.</p>
</div>

<!-- portfolio -->
<h2 class="abs display portfolio-title">Explore Our Building<br>&amp; Heavy Project Portfolio</h2>
<a class="abs btn-outline" style="left:617px;top:2251px;width:118px;height:39px;">VIEW ALL</a>
<svg class="btn-arrow" style="left:726px;top:2259px" width="34" height="24" viewBox="0 0 34 24"><path d="M0 12H32M23 3l9 9-9 9" fill="none" stroke="#1a7fd4" stroke-width="1.5"/></svg>

<div class="abs tile" style="left:130px;top:2336px;background:linear-gradient(180deg,#3f6fb8 0%,#7d9cc9 40%,#b8bcc0 60%,#8d8a84 100%)" role="img" aria-label="Photograph of a metal-clad commercial building exterior under blue sky"></div>
<div class="abs tile" style="left:439px;top:2336px;background:linear-gradient(180deg,#d9dbdd 0%,#b7bcc0 50%,#6f747a 100%)" role="img" aria-label="Photograph of a glass-walled office meeting room"></div>
<div class="abs tile" style="left:130px;top:2564px;background:linear-gradient(180deg,#e8e6e4 0%,#d4d0cc 55%,#8e8580 100%)" role="img" aria-label="Photograph of a bright lobby with ring pendant lights and lounge chairs"></div>
<div class="abs tile" style="left:439px;top:2564px;background:linear-gradient(90deg,#4d5052 0%,#8a8e90 45%,#6d5a48 80%,#3e3b38 100%)" role="img" aria-label="Photograph of an office corridor with glass partitions"></div>

<div class="abs timeline"></div>
<div class="abs timeline-active"></div>
<div class="abs entry active" style="top:2365px"><h3>Lorem ipsum dolor sit amet</h3><p>Sed ut perspiciatis unde omnis iste natus error sit voluptatem accusantium dolorem que laudantium, totam rem aperiam, eaque ipsa</p></div>
<div class="abs divider" style="top:2486px"></div>
<div class="abs entry" style="top:2521px"><h3>Lorem ipsum dolor sit amet</h3><p>Sed ut perspiciatis unde omnis iste natus error sit voluptatem accusantium dolorem que laudantium, totam rem aperiam, eaque ipsa</p></div>
<div class="abs divider" style="top:2654px"></div>
<div class="abs entry" style="top:2683px"><h3>Lorem ipsum dolor sit amet</h3><p>Sed ut perspiciatis unde omnis iste natus error sit voluptatem accusantium dolorem que laudantium, totam rem aperiam, eaque ipsa</p></div>

<!-- footer + cta -->
<div class="abs footer"></div>
<div class="abs cta" role="img" aria-label="Blue-tinted photograph of a commercial storefront"></div>
<h2 class="abs display cta-title">Lorem ipsum dolor sit amet consectetur<br>adipiscing elit sed do eiusmod tempor</h2>
<a class="abs cta-btn">CONTACT US <svg width="32" height="20" viewBox="0 0 32 20"><path d="M0 10H30M21 2l8 8-8 8" fill="none" stroke="#1a7fd4" stroke-width="1.6"/></svg></a>

<div class="abs foot-mark"></div>
<div class="abs foot-name">R &amp; K<br>GROUP</div>

<div class="abs foot-head" style="left:395px;top:3236px">MENU</div>
<ul class="abs foot-links"><li>HOME</li><li>ABOUT US</li><li>PROJECTS</li><li>CONTACT US</li></ul>

<div class="abs foot-head" style="left:624px;top:3236px">CONTACT US</div>
<div class="abs foot-item" style="left:624px;top:3271px"><span class="foot-ico"><svg width="10" height="13" viewBox="0 0 10 13"><path d="M5 12S1 7 1 5a4 4 0 0 1 8 0c0 2-4 7-4 7z" fill="#262626"/><circle cx="5" cy="5" r="1.5" fill="#fff"/></svg></span><span>2215 Harbourview Road<br>Halifax, NS B3H 4R2</span></div>
<div class="abs foot-item" style="left:624px;top:3321px"><span class="foot-ico"><svg width="12" height="12" viewBox="0 0 12 12"><path d="M2 1h3l1 3-2 1a7 7 0 0 0 3 3l1-2 3 1v3c-6 0-9-3-9-9z" fill="#262626"/></svg></span><span>Call Us<br>902.555.0147</span></div>
<div class="abs foot-item" style="left:624px;top:3371px"><span class="foot-ico"><svg width="12" height="9" viewBox="0 0 12 9"><rect x="0" y="0" width="12" height="9" rx="1" fill="#262626"/><path d="M1 1l5 4 5-4" fill="none" stroke="#fff" stroke-width="1"/></svg></span><span>E mail Us<br>info@rkgroupdevelopments.ca</span></div>

<div class="abs foot-head" style="left:960px;top:3236px">FOLLOW US</div>
<div class="abs foot-item" style="left:960px;top:3271px"><span class="foot-ico"></span><span>Like us on<br>FRIENDWALL</span></div>
<div class="abs foot-item" style="left:960px;top:3321px"><span class="foot-ico"></span><span>Follow us on<br>CHIRPER</span></div>
<div class="abs foot-item" style="left:960px;top:3371px"><span class="foot-ico"></span><span>Follow us on<br>WORKLINK</span></div>

<div class="abs foot-rule"></div>
<p class="abs copyright">Copyright © 2021 All Rights Reserved</p>

</body>
</html>
```